(Wordpress)Website Design - No requirements! Sign Your name at the bottom of the site!

Dear Designer,

I am looking for a designer who is interested in a long-term business realtionship.
I already have 2 more designs to get done IMMEDIATELY after this website..
1.) An email brochure matching the website theme.
2.) A Billboard. BOTH MATCHING THE WEBSITE THEME

For this project, a bonus WILL be given.

Go to vaultnest.com as Site Inspiration

Please take this opportunity to design an existing wordpress website, FUNDSWIFTLANE.com, in whatever form your creativity takes you

I have no requirements other than a CREATIVE and OUT-OF -THE-BOX Design. Something Pretty and Eye Catching; a website that someone logs onto and doesnt want to leave

I have purchased a theme called velorant. You dont need to use it...But Info can be found at

http://skinbazaar.example/item/velorant-premium-wordpress-theme/full_screen_preview/482715

I have attached my logos and a PDF with a short story about what our company does.

Thank You,
-Tobin
PS I HAVE ANOTHER 2 DESIGNS TO DO AFTER THIS PROJECT.
also, IF YOU KNOW OF SOMEONE WHO DOES SEO WORK, I AM LOOKING FOR A FULL-TIME EMPLOYEE

Target Market(s)

Business Owners in a state of finacial NEED

Industry/Entity Type

Business

Requirements
Must have
• COLORFUL, EYE CATCHING

```html
<!DOCTYPE html>
<html lang="en">
<head>
<meta charset="utf-8">
<title>FundSwift Lane</title>
<link rel="stylesheet" href="https://fonts.googleapis.com/css2?family=Source+Sans+3:wght@400;600;700&family=Arimo:ital,wght@0,400;0,700;1,400&display=swap">
<style>
:root{
  --navy:#0c3a7a;
  --nav:#123f86;
  --nav-dark:#0a2f66;
  --band:#1b4f9c;
  --band-dark:#0f3a7c;
  --green:#1f8a1f;
  --green-dark:#146414;
  --title:#1c4e93;
  --ink:#1a1a1a;
  --grey:#555;
  --light:#f3f3f3;
  --footer:#14428c;
  --footer-dark:#0c3270;
  --brand-green:#7a9a52;
}
*{margin:0;padding:0;box-sizing:border-box}
html,body{width:780px;height:1200px;overflow:hidden;background:#fff}
.page{position:relative;width:780px;height:1200px;font-family:"Arimo",Arial,sans-serif;color:var(--ink)}
.abs{position:absolute}
.sans{font-family:"Source Sans 3",Arial,sans-serif}

.brand{left:94px;top:22px;display:flex;align-items:center;gap:8px}
.brand-mark{width:30px;height:30px;background:var(--title);border-radius:50%}
.brand-name{font-family:"Source Sans 3",Arial,sans-serif;font-size:36px;font-weight:600;color:var(--title);letter-spacing:-0.5px}

.account{left:540px;top:7px;font-size:9px;display:flex;align-items:center;gap:6px}
.login{width:67px;height:23px;background:var(--nav);color:#fff;font-family:"Source Sans 3",Arial,sans-serif;font-size:12px;display:flex;align-items:center;padding-left:10px;border-radius:0 0 3px 3px}
.contact{right:95px;top:30px;text-align:right;font-size:9px;line-height:11.5px;font-weight:700}
.contact u{font-weight:700}

.nav{left:0;top:123px;width:780px;height:26px;background:linear-gradient(var(--nav),var(--nav-dark));border-top:2px solid #1f56a8}
.nav a{position:absolute;top:0;height:24px;line-height:24px;transform:translateX(-50%);color:#a9c3ea;font-size:8.5px;text-decoration:none;font-family:"Source Sans 3",Arial,sans-serif;letter-spacing:-0.2px}
.nav a.active{background:#2b5ea9;color:#fff;width:39px;text-align:center}

.hero{left:93px;top:175px;width:593px;height:211px;background:linear-gradient(90deg,#f4f4f4,#e6e6e6);border:1px solid #ccc;border-bottom:none;overflow:hidden}
.hero-photo{position:absolute;left:0;top:0;width:317px;height:211px;background:linear-gradient(135deg,#d9d2c8,#b48e6c 45%,#e9e9e9)}
.hero-copy{position:absolute;left:340px;top:34px;width:245px;text-align:center;font-family:"Source Sans 3",Arial,sans-serif;font-size:19px;line-height:21px;color:#111}
.hero-copy .today{color:var(--green);font-weight:700;font-size:26px}
.checks{position:absolute;left:354px;top:112px;width:240px;font-family:"Source Sans 3",Arial,sans-serif;font-size:11.5px;display:grid;grid-template-columns:111px 1fr;row-gap:3px}
.checks span::before{content:"✓";font-size:13px;margin-right:5px;color:#333}
.apply-btn{position:absolute;left:329px;top:168px;width:136px;height:31px;background:linear-gradient(var(--green),var(--green-dark));border:1px solid #0d4a0d;color:#fff;font-family:"Source Sans 3",Arial,sans-serif;font-size:16px;display:flex;align-items:center;justify-content:center;gap:8px;box-shadow:0 2px 3px rgba(0,0,0,.35)}
.dots{position:absolute;left:539px;top:194px;display:flex;gap:4px}
.dots i{width:7px;height:7px;border-radius:50%;background:#bbb;border:1px solid #999}

.apply-band{left:85px;top:386px;width:607px;height:102px;background:linear-gradient(var(--band),var(--band-dark))}
.apply-title{position:absolute;left:0;top:8px;width:607px;text-align:center;font-family:"Source Sans 3",Arial,sans-serif;font-size:26px;font-weight:600;color:#fff;letter-spacing:-0.5px}
.field{position:absolute;top:51px;width:98px;height:20px;background:#fff;border-radius:3px;font-size:8px;padding-left:7px;line-height:20px;color:#222}
.submit{position:absolute;left:472px;top:51px;width:86px;height:19px;background:linear-gradient(#2aa02a,var(--green-dark));border:1px solid #fff;color:#fff;font-family:"Source Sans 3",Arial,sans-serif;font-weight:700;font-size:13px;text-align:center;line-height:17px}
.agree{position:absolute;left:41px;top:80px;font-size:8.5px;color:#d6e2f5;display:flex;gap:6px;align-items:center}
.agree i{width:8px;height:8px;background:#d6e2f5;border-radius:1px}

.steps{left:99px;top:498px;width:580px;height:89px;background:linear-gradient(var(--band),var(--band-dark));display:flex}
.step{height:89px;display:flex;align-items:center;gap:10px;padding-left:5px;color:#fff;font-family:"Source Sans 3",Arial,sans-serif;border-right:1px solid #0a2d62}
.step:last-child{border-right:none}
.step-num{font-size:24px;line-height:21px;text-align:center;letter-spacing:-1px}
.step-text{font-size:13.5px;line-height:18px;letter-spacing:-0.4px}
.step-text b{font-weight:600}

.content{left:93px;top:606px;width:591px;height:369px;background:#fff;border:1px solid #ddd;box-shadow:0 1px 4px rgba(0,0,0,.18)}
.h2{position:absolute;font-family:"Source Sans 3",Arial,sans-serif;font-size:19px;color:var(--title);letter-spacing:-0.3px}
.rule{position:absolute;height:1px;background:#cfcfcf}
.handshake{position:absolute;left:22px;top:61px;width:129px;height:106px;background:linear-gradient(135deg,#f4f4f4,#cfd3d8 60%,#6b6b6b)}
.lead{position:absolute;left:163px;top:60px;width:177px;font-size:7.3px;line-height:9.8px;font-weight:700}
.para{position:absolute;font-size:7.3px;line-height:10.7px;color:var(--grey)}
.quote-mark{position:absolute;left:22px;top:308px;font-family:"Source Sans 3",Arial,sans-serif;font-size:60px;line-height:50px;color:var(--title);font-weight:700}
.quote{position:absolute;left:58px;top:314px;width:225px;font-size:7.3px;line-height:10.8px;font-style:italic}
.author{position:absolute;left:55px;top:347px;font-size:8px;font-weight:700;font-style:italic}
.see-more{position:absolute;left:291px;top:347px;font-size:7.3px;color:#777;display:flex;align-items:center;gap:4px}
.date{position:absolute;left:372px;top:63px;width:45px;height:14px;background:#eee;border:1px solid #ddd;font-size:8px;line-height:12px;text-align:center}
.news-title{position:absolute;left:423px;top:64px;font-size:8px;color:var(--title)}
.read-more{position:absolute;left:372px;top:130px;font-size:7px;font-weight:700;color:#333}
.money{position:absolute;left:372px;top:166px;width:215px;height:203px;background:linear-gradient(#fafafa,#d8d4cf 40%,#4c5a6e)}

.footer{left:0;top:1003px;width:780px;height:197px;background:linear-gradient(var(--footer-dark),var(--footer) 40%,var(--footer))}
.col{position:absolute;top:18px;color:#fff}
.col h4{font-family:"Arimo",Arial,sans-serif;font-weight:400;font-size:10px;margin-bottom:8px}
.col li{list-style:none;font-size:8px;color:#d9e3f3;margin-bottom:8.2px;padding-left:8px;position:relative}
.col li::before{content:"";position:absolute;left:0;top:2px;border-left:3px solid #fff;border-top:2.5px solid transparent;border-bottom:2.5px solid transparent}
.follow{left:520px;top:1151px;font-size:10px;font-weight:700;color:#fff;display:flex;align-items:center;gap:8px}
.social{width:22px;height:22px;border-radius:3px}
</style>
</head>
<body>
<div class="page">

  <div class="abs brand">
    <span class="brand-mark"></span>
    <span class="brand-name">FundSwift Lane</span>
  </div>

  <div class="abs account">
    <span>Already rejistered?</span>
    <span class="login">LOGIN</span>
  </div>
  <div class="abs contact">
    <u>Begin Online</u><br>Or<br>Call Us Now! (800)555-0142
  </div>

  <nav class="abs nav">
    <a class="active" style="left:121px">HOME</a>
    <a style="left:186px">ABOUT US</a>
    <a style="left:256px">SERVICES</a>
    <a style="left:318px">FAQ'S</a>
    <a style="left:395px">OUR ADVANTAGE</a>
    <a style="left:485px">CONTACT US</a>
  </nav>

  <section class="abs hero">
    <div class="hero-photo" role="img" aria-label="Photo of a smiling couple lying on the floor using a laptop"></div>
    <div class="hero-copy">Apply <span class="today">TODAY</span> for fast Cash<br>Loans straight to you!<br>Upto $750 Available Now</div>
    <div class="checks">
      <span>Instant Transfer</span><span>Instant Decision</span>
      <span>Safe &amp; Secure</span><span>Choose Your Amount</span>
    </div>
    <div class="apply-btn">Apply Now!
      <svg width="12" height="14" viewBox="0 0 12 14"><rect x="0" y="1" width="3" height="12" fill="#fff"/><path d="M5 1 L12 7 L5 13Z" fill="#fff"/></svg>
    </div>
    <div class="dots"><i></i><i></i><i></i><i></i></div>
  </section>

  <section class="abs apply-band">
    <svg class="abs" style="left:222px;top:10px" width="38" height="36" viewBox="0 0 38 36"><path d="M2 2 L19 18 L36 2 L36 12 L19 28 L2 12Z" fill="#2f86d8"/><path d="M6 16 L19 28 L32 16 L32 22 L19 34 L6 22Z" fill="#2f86d8"/></svg>
    <svg class="abs" style="left:472px;top:10px" width="38" height="36" viewBox="0 0 38 36"><path d="M2 2 L19 18 L36 2 L36 12 L19 28 L2 12Z" fill="#2f86d8"/><path d="M6 16 L19 28 L32 16 L32 22 L19 34 L6 22Z" fill="#2f86d8"/></svg>
    <div class="apply-title">Apply Today!</div>
    <div class="field" style="left:40px">First Name</div>
    <div class="field" style="left:148px">Last Name</div>
    <div class="field" style="left:256px">Phone</div>
    <div class="field" style="left:364px">Email</div>
    <div class="submit">SUBMIT</div>
    <div class="agree"><i></i>I AGREE TO TERMS AND CONDITIONS</div>
  </section>

  <section class="abs steps">
    <div class="step" style="width:189px"><div class="step-num">Step<br>1</div><div class="step-text"><b>Apply Now</b><br>Completely online</div></div>
    <div class="step" style="width:200px"><div class="step-num">Step<br>2</div><div class="step-text"><b>Get Approved</b><br>Recieve Fast Approval</div></div>
    <div class="step" style="width:191px"><div class="step-num">Step<br>3</div><div class="step-text"><b>Get Funds</b><br>In Less than One Hour</div></div>
  </section>

  <section class="abs content">
    <h2 class="h2" style="left:19px;top:12px">Welcome to FundSwift Lane</h2>
    <div class="rule" style="left:19px;top:41px;width:323px"></div>
    <div class="handshake" role="img" aria-label="Photo of a business handshake over paperwork"></div>
    <p class="lead">Dummy text we are a company based in Woking, Surrey who are a collective group of experienced trades people in every area of the building industry from the initial contact to the completion with the local authorities.</p>
    <p class="para" style="left:163px;top:117px;width:177px;line-height:9.8px">We offer expert advice that will make a build easy to understand but also finished to a high quality standard. We also offer architectural services and we have a proven track record of quality and sustainability.</p>
    <p class="para" style="left:22px;top:180px;width:314px">Remember; Build Smart, Choose Impact. Benfits we can offer you the customer we can effectively plan the build from the very start to completion with the local authority (council) to handover effortlessly as experience has taught us planning in any project is the key to make the build successful . Please visit our profile to see similar projects and thoughts of our customers Hard working team of individuals with over 15 years experience in different fields of the building trade site managers / partners are muti-skilled and these skills can be called upon to make jobs run with out delays In house Part P registered company Good after sales service.</p>
    <h2 class="h2" style="left:19px;top:270px">Client Testimonials</h2>
    <div class="quote-mark">“</div>
    <p class="quote">"It is a long established fact that a reader will be distracted by the readable content of a page when looking at its layout.Content here, content here', making it look like readable English."</p>
    <div class="author">-Dana Welles</div>
    <div class="see-more">See more
      <svg width="16" height="14" viewBox="0 0 16 14"><path d="M3 1 L13 7 L3 13" fill="none" stroke="#8aa6cc" stroke-width="1.5"/></svg>
    </div>

    <h2 class="h2" style="left:372px;top:12px">News</h2>
    <div class="rule" style="left:372px;top:41px;width:190px"></div>
    <div class="date">12. 01. 12</div>
    <div class="news-title">Dummy News</div>
    <p class="para" style="left:372px;top:86px;width:196px;font-size:6.6px;line-height:9.7px">Dummy News we offer expert advice that will make a build easy to understand but also finished to a high quality standard. We also offer architectural services and we have a proven track record of quality and sustainability.</p>
    <div class="read-more">Read More&gt;&gt;</div>
    <div class="money" role="img" aria-label="Photo of a cheerful group reaching up for falling banknotes"></div>
  </section>

  <footer class="abs footer">
    <div class="col" style="left:124px"><h4>Types Of loans</h4><ul><li>Payday loans</li><li>Fast loan</li><li>Compare All Payday Lenders</li><li>Best Payday Loans</li></ul></div>
    <div class="col" style="left:269px"><h4>Fast Loans</h4><ul><li>Same Day Loans Online</li><li>Easy Loan Today</li><li>Payday Advance</li><li>Faxless Payday Loans</li></ul></div>
    <div class="col" style="left:403px"><h4>Quick Advance</h4><ul><li>Payday Cash Advances</li><li>Short term loans</li><li>Payday Cash</li><li>Weekend Cash Payments</li></ul></div>
    <div class="col" style="left:553px"><h4>Online Loans</h4><ul><li>London Cash Loan</li><li>Fast Cash Loan</li><li>US Payday Loans</li><li>Cash Advances</li></ul></div>
  </footer>
  <div class="abs follow">Follow Us:
    <span class="social" style="background:#3a63a8"></span>
    <span class="social" style="background:#3aa6d8"></span>
  </div>

</div>
</body>
</html>
```